Tot Tumble Program Marketing Material

We are seeking a graphic designer for our new gymnastics program across the state of Victoria in Australia. The program is called Tot Tumble, which is aimed at babies (girls and boys) aged between 4 and 12 months. The program and branding is targeted at Mums and Dads with babies.

The program is short, fun, friendly and valuable for babies developing basic skills – for example, crawling. The classes enable babies to progress with moving at their own pace and provide parents with skills to help their child move, as well as knowledge to understand the benefits of gymnastics for everybody at the young age, including babies.

Items to be developed in the following formats:
1. Please create documents in these formats: Adobe Photoshop, Adobe InDesign, Microsoft Publisher
2. Please create logos in horizontal and vertical layout in the following formats: JPEG and EPS.
3. Please provide brand information so we can create other documents with the same branding. The information we need is: Font Type, Font Size, Colours (PMS and RGB format).

Marketing Material
1. General Poster: assist sports clubs with advertising the program in their area. Format to allow for both online distribution through a website and in hard copy.
a. Size – A2.
b. Allow space in the design so a sports centre can add their organisation logo at the bottom.

2. General Brochure: assist sports clubs with advertising the program in their area. Format to allow for both online distribution through a website and in hard copy.
a. Size – A5.

3. Brand professional photos: add colour logo to photos provided.

Logos
4. Colour Logo: please follow the same style as the Floorwork League logo. We are happy with the colours and feel as our current Tot Tumble logo. This is attached for you.

5. Black and White Logo: same as above but in black and white format.

How will the package be used?
1. Package will be used by gymnastics clubs online and in hard copy.
2. Professional hard copies of the brochure, poster and handouts will be made by clubs.

```html
<!DOCTYPE html>
<html lang="en">
<head>
<meta charset="utf-8">
<title>Tot Tumble – Poster Layouts</title>
<link rel="stylesheet" href="https://fonts.googleapis.com/css2?family=Bubblegum+Sans&family=Gochi+Hand&family=Aldrich&family=Open+Sans:wght@700&display=swap">
<style>
  :root {
    --backdrop: #efefef;
    --frame-green: #7cc242;
    --paper: #ffffff;
    --title-blue: #3d79b8;
    --body-green: #7cbf2e;
    --pill-blue: #5a86b6;
    --pill-edge: #8fb1d6;
    --brand-navy: #1f3f8a;
    --logo-grey: #6b6b6b;
    --bar-orange: #ef7f3c;
    --white: #ffffff;
  }
  * { margin: 0; padding: 0; box-sizing: border-box; }
  html, body { width: 1200px; height: 849px; overflow: hidden; }
  body { background: var(--backdrop); position: relative; }

  .poster {
    position: absolute;
    top: 54px;
    width: 527px;
    height: 741px;
    background: var(--paper);
    border: 14px solid var(--frame-green);
  }
  .poster--logo-bottom { left: 60px; }
  .poster--logo-top { left: 614px; }

  .poster > * { position: absolute; }

  .photo { width: 151px; height: 151px; }
  .photo--col1 { left: 16px; }
  .photo--col2 { left: 174px; }
  .photo--col3 { left: 331px; }

  .photo--crawl-mat { background: linear-gradient(160deg, #9fb6c8 0%, #3f9f4a 45%, #2e6fb8 100%); }
  .photo--bow-baby { background: linear-gradient(170deg, #c9b79a 0%, #f2e2a0 45%, #4aa64a 100%); }
  .photo--crawl-blue { background: linear-gradient(170deg, #d9cfc3 0%, #e8b590 40%, #2f8fc4 100%); }
  .photo--standing-help { background: linear-gradient(160deg, #7aa0c4 0%, #e9c6b4 50%, #d94f6a 100%); }
  .photo--lift { background: linear-gradient(160deg, #b8b0a8 0%, #e8c4a8 50%, #5b6b7a 100%); }
  .photo--ball-play { background: linear-gradient(160deg, #e8a7a0 0%, #d85a6e 50%, #2aa39a 100%); }

  .headline {
    left: 0; right: 0;
    text-align: center;
    font-family: "Bubblegum Sans", cursive;
    font-size: 33px;
    line-height: 36px;
    color: var(--title-blue);
    letter-spacing: 0.5px;
  }
  .intro {
    left: 20px; right: 20px;
    text-align: center;
    font-family: "Gochi Hand", cursive;
    font-size: 17px;
    line-height: 26.5px;
    color: var(--body-green);
  }

  .benefit-grid {
    left: 20px;
    width: 472px;
    display: grid;
    grid-template-columns: 224px 225px;
    column-gap: 8px;
    row-gap: 6px;
  }
  .benefit {
    height: 28.5px;
    border-radius: 7px;
    background: var(--pill-blue);
    border: 1.5px solid var(--pill-edge);
    color: var(--white);
    font-family: "Gochi Hand", cursive;
    font-size: 16px;
    line-height: 25px;
    text-align: center;
  }

  .brand {
    display: flex;
    align-items: center;
    gap: 10px;
  }
  .brand-dot { border-radius: 50%; background: var(--brand-navy); flex: none; }
  .brand-name {
    font-family: "Gochi Hand", cursive;
    font-size: 20px;
    color: var(--brand-navy);
    white-space: nowrap;
  }

  .logo-space {
    font-family: "Aldrich", sans-serif;
    font-size: 29px;
    line-height: 31px;
    color: var(--logo-grey);
    text-align: center;
  }

  .web-bar {
    left: 16px;
    top: 684px;
    width: 466px;
    height: 19px;
    border-radius: 9px;
    background: var(--bar-orange);
    color: var(--white);
    font-family: "Open Sans", sans-serif;
    font-weight: 700;
    font-size: 11px;
    line-height: 19px;
    text-align: center;
  }

  /* logo-bottom variant */
  .poster--logo-bottom .photo-row--top { top: 13px; }
  .poster--logo-bottom .photo-row--bottom { top: 438px; }
  .poster--logo-bottom .headline { top: 175px; }
  .poster--logo-bottom .intro { top: 214px; }
  .poster--logo-bottom .benefit-grid { top: 297px; }
  .poster--logo-bottom .brand { left: 70px; top: 606px; }
  .poster--logo-bottom .brand-dot { width: 66px; height: 66px; }
  .poster--logo-bottom .logo-space { left: 275px; top: 607px; width: 90px; }

  /* logo-top variant */
  .poster--logo-top .brand { left: 77px; top: 10px; }
  .poster--logo-top .brand-dot { width: 86px; height: 86px; }
  .poster--logo-top .logo-space { left: 365px; top: 20px; width: 86px; }
  .poster--logo-top .photo-row--top { top: 109px; }
  .poster--logo-top .photo-row--bottom { top: 525px; height: 151px; }
  .poster--logo-top .headline { top: 266px; }
  .poster--logo-top .intro { top: 301px; }
  .poster--logo-top .benefit-grid { top: 385px; }
</style>
</head>
<body>

<section class="poster poster--logo-bottom">
  <div class="photo photo--col1 photo-row--top photo--crawl-mat" role="img" aria-label="Baby crawling over a green and blue gym mat"></div>
  <div class="photo photo--col2 photo-row--top photo--bow-baby" role="img" aria-label="Baby girl with a bow lying on a colourful mat"></div>
  <div class="photo photo--col3 photo-row--top photo--crawl-blue" role="img" aria-label="Smiling baby in a blue top crawling"></div>

  <h1 class="headline">WHY TOT TUMBLE?</h1>
  <p class="intro">Tot Tumble provides a strong foundation for their critical early years. This period of your child's life will influence their movement abilities later. The development areas the program</p>

  <ul class="benefit-grid">
    <li class="benefit">Brain Development</li>
    <li class="benefit">Body Awareness</li>
    <li class="benefit">Social interaction</li>
    <li class="benefit">Vestibular stimulation</li>
    <li class="benefit">Balance</li>
    <li class="benefit">Core strength</li>
    <li class="benefit">Fine motor skills</li>
    <li class="benefit">Sensory system</li>
  </ul>

  <div class="photo photo--col1 photo-row--bottom photo--standing-help" role="img" aria-label="Parent helping a baby stand"></div>
  <div class="photo photo--col2 photo-row--bottom photo--lift" role="img" aria-label="Coach lifting a baby during class"></div>
  <div class="photo photo--col3 photo-row--bottom photo--ball-play" role="img" aria-label="Baby playing with a striped ball"></div>

  <div class="brand">
    <span class="brand-dot"></span>
    <span class="brand-name">Tot Tumble</span>
  </div>
  <div class="logo-space">LOGO<br>SPACE</div>

  <div class="web-bar">www.tottumble.com</div>
</section>

<section class="poster poster--logo-top">
  <div class="brand">
    <span class="brand-dot"></span>
    <span class="brand-name">Tot Tumble</span>
  </div>
  <div class="logo-space">LOGO<br>SPACE</div>

  <div class="photo photo--col1 photo-row--top photo--crawl-mat" role="img" aria-label="Baby crawling over a green and blue gym mat"></div>
  <div class="photo photo--col2 photo-row--top photo--bow-baby" role="img" aria-label="Baby girl with a bow lying on a colourful mat"></div>
  <div class="photo photo--col3 photo-row--top photo--crawl-blue" role="img" aria-label="Smiling baby in a blue top crawling"></div>

  <h1 class="headline">WHY TOT TUMBLE?</h1>
  <p class="intro">Tot Tumble provides a strong foundation for their critical early years. This period of your child's life will influence their movement abilities later. The development areas the program</p>

  <ul class="benefit-grid">
    <li class="benefit">Brain Development</li>
    <li class="benefit">Body Awareness</li>
    <li class="benefit">Social interaction</li>
    <li class="benefit">Vestibular stimulation</li>
    <li class="benefit">Balance</li>
    <li class="benefit">Core strength</li>
    <li class="benefit">Fine motor skills</li>
    <li class="benefit">Sensory system</li>
  </ul>

  <div class="photo photo--col1 photo-row--bottom photo--standing-help" role="img" aria-label="Parent helping a baby stand"></div>
  <div class="photo photo--col2 photo-row--bottom photo--lift" role="img" aria-label="Coach lifting a baby during class"></div>
  <div class="photo photo--col3 photo-row--bottom photo--ball-play" role="img" aria-label="Baby playing with a striped ball"></div>

  <div class="web-bar">www.tottumble.com</div>
</section>

</body>
</html>
```